Thank you for shopping with us business card

We would like a thank you card for our rebranded business. We used to be "Brindle Goods" but are now "Marlow Finds. Old thank you card and new logo will be attached for reference. New thank you card does not have to be same design as old thank you card, but please use new logo.
Shopmart URL is now marlowfinds.shopmart.example
Instagram is @Marlow_Finds
Email is marlowfinds@mailbox.example
Thank you!

Contact Information for Business Card

Shopmart site, email, Instagram

```html
<!DOCTYPE html>
<html lang="en">
<head>
<meta charset="utf-8">
<title>Marlow Finds – Thank You Card</title>
<link href="https://fonts.googleapis.com/css2?family=Bebas+Neue&family=Montserrat:wght@400;600&display=swap" rel="stylesheet">
<style>
  :root {
    --backdrop: #e9e6e1;
    --card-black: #111113;
    --card-black-sheen: #2a2a2e;
    --brand-grey: #b9b9bd;
    --paper: #ffffff;
    --ink: #1b1b1b;
    --band: #58585a;
    --band-text: #f2f2f2;
    --contact-text: #3a3a3a;
  }
  * { margin: 0; padding: 0; box-sizing: border-box; }
  html, body {
    width: 1200px;
    height: 913px;
    overflow: hidden;
    background: var(--backdrop);
  }
  .sheet {
    width: 1200px;
    height: 913px;
    display: flex;
    align-items: center;
    justify-content: center;
    gap: 40px;
  }
  .card {
    width: 540px;
    height: 309px;
    border-radius: 3px;
    overflow: hidden;
    position: relative;
    box-shadow: 0 6px 18px rgba(0,0,0,0.18);
  }

  /* Front */
  .card-front {
    background: linear-gradient(135deg, var(--card-black-sheen) 0%, var(--card-black) 45%, var(--card-black) 100%);
    display: flex;
    align-items: center;
    justify-content: center;
  }
  .brand-name {
    font-family: "Montserrat", sans-serif;
    font-weight: 600;
    font-size: 34px;
    letter-spacing: 1px;
    color: var(--brand-grey);
    text-transform: uppercase;
  }

  /* Back */
  .card-back {
    background: var(--paper);
    display: flex;
    flex-direction: column;
  }
  .thanks {
    flex: 0 0 142px;
    display: flex;
    flex-direction: column;
    align-items: center;
    justify-content: flex-end;
    padding-bottom: 12px;
    font-family: "Bebas Neue", sans-serif;
    color: var(--ink);
    line-height: 0.9;
  }
  .thanks-main { font-size: 72px; letter-spacing: 1px; }
  .thanks-sub { font-size: 42px; letter-spacing: 1px; }
  .message-band {
    flex: 0 0 98px;
    background: var(--band);
    display: flex;
    flex-direction: column;
    align-items: center;
    justify-content: center;
    text-align: center;
    padding: 0 12px;
    font-family: "Montserrat", sans-serif;
    font-size: 12.5px;
    line-height: 1.7;
    color: var(--band-text);
  }
  .message-line { white-space: nowrap; }
  .contacts {
    flex: 1;
    display: flex;
    align-items: center;
    justify-content: space-between;
    padding: 0 16px;
    font-family: "Montserrat", sans-serif;
    font-size: 10px;
    color: var(--contact-text);
  }
  .contact-item { display: flex; align-items: center; gap: 6px; white-space: nowrap; }
  .contact-icon { width: 14px; height: 14px; flex: 0 0 14px; }
</style>
</head>
<body>
<main class="sheet">
  <section class="card card-front" aria-label="Card front">
    <span class="brand-name">Marlow Finds</span>
  </section>

  <section class="card card-back" aria-label="Card back">
    <header class="thanks">
      <span class="thanks-main">Thank You</span>
      <span class="thanks-sub">For Purchase</span>
    </header>
    <div class="message-band">
      <span class="message-line">Your purchase made my day and I hope this package brighten yours.</span>
      <span class="message-line">Please come back and leave a review!</span>
    </div>
    <footer class="contacts">
      <span class="contact-item">
        <svg class="contact-icon" viewBox="0 0 14 14" aria-hidden="true">
          <circle cx="7" cy="7" r="7" fill="var(--band)"/>
          <rect x="3.5" y="4.5" width="7" height="5" fill="none" stroke="#fff" stroke-width="1"/>
          <polyline points="3.5,4.5 7,7.5 10.5,4.5" fill="none" stroke="#fff" stroke-width="1"/>
        </svg>
        marlowfinds@mailbox.example
      </span>
      <span class="contact-item">
        <svg class="contact-icon" viewBox="0 0 14 14" aria-hidden="true">
          <circle cx="7" cy="7" r="7" fill="var(--band)"/>
          <circle cx="7" cy="7" r="3.8" fill="none" stroke="#fff" stroke-width="1"/>
          <line x1="3.2" y1="7" x2="10.8" y2="7" stroke="#fff" stroke-width="0.8"/>
          <ellipse cx="7" cy="7" rx="1.6" ry="3.8" fill="none" stroke="#fff" stroke-width="0.8"/>
        </svg>
        marlowfinds.shopmart.example
      </span>
      <span class="contact-item">
        <svg class="contact-icon" viewBox="0 0 14 14" aria-hidden="true">
          <circle cx="7" cy="7" r="7" fill="var(--band)"/>
        </svg>
        @Marlow_Finds
      </span>
    </footer>
  </section>
</main>
</body>
</html>
```